Plakate für Podologie - Medizinische Fusspflege
Zielgruppe
Podologie - Medizinische Fusspflege. Zielgruppe sind Kinder bis und mit ältere Menschen.
Aufgabenstellung
Möchte ein modernes, aber auch klassisches Design, dass Professionalität & medizinische Fundiertheit ausstrahlt. Man soll sehen, dass es medizinisch ist und nicht verwechselbar mit kosmetischer Fusspflege.

```html
<!DOCTYPE html>
<html lang="de">
<head>
<meta charset="utf-8">
<title>Solvita – Medizinische Podologie</title>
<link href="https://fonts.googleapis.com/css2?family=Poppins:wght@400;500;700;800&display=swap" rel="stylesheet">
<style>
  :root {
    --teal: #135a58;
    --teal-soft: #dcebe9;
    --green: #69ac55;
    --ink: #1b1b1b;
    --paper: #ffffff;
    --backdrop: #cccccc;
  }
  * { margin: 0; padding: 0; box-sizing: border-box; }
  html, body {
    width: 1200px; height: 960px; overflow: hidden;
    background: var(--backdrop);
    font-family: "Poppins", sans-serif;
  }
  .poster {
    position: absolute; left: 302px; top: 50px;
    width: 608px; height: 861px;
    background: var(--paper);
    overflow: hidden;
  }
  .header {
    position: absolute; left: 0; top: 0; width: 100%; height: 154px;
    background: var(--teal);
    display: flex; flex-direction: column; align-items: center; justify-content: center;
    color: var(--paper);
  }
  .brand {
    display: flex; align-items: center; gap: 14px;
  }
  .brand-dot {
    width: 34px; height: 34px; border-radius: 50%; background: var(--paper);
  }
  .brand-name {
    font-size: 46px; font-weight: 500; line-height: 1; letter-spacing: -0.5px;
  }
  .brand-tagline {
    margin-top: 10px; font-size: 12px; font-weight: 500; letter-spacing: 2px;
  }
  .headline {
    position: absolute; top: 186px; width: 100%; text-align: center;
    font-size: 31px; font-weight: 700; color: var(--teal); letter-spacing: -0.2px;
  }
  .intro {
    position: absolute; top: 236px; width: 100%; text-align: center;
    font-size: 21px; font-weight: 400; line-height: 31px; color: var(--ink);
  }
  .services { position: absolute; left: 88px; top: 322px; list-style: none; }
  .service {
    display: flex; align-items: center; height: 58.6px;
  }
  .service-icon {
    width: 50px; height: 47px; border-radius: 8px;
    background: var(--teal-soft); flex: none;
  }
  .service-name {
    margin-left: 27px; font-size: 22px; font-weight: 700; color: var(--teal);
  }
  .audience {
    position: absolute; top: 645px; width: 100%; text-align: center;
    font-size: 21.5px; font-weight: 700; color: var(--teal); letter-spacing: -0.2px;
  }
  .credentials {
    position: absolute; top: 686px; width: 100%; text-align: center;
    font-size: 16.5px; font-weight: 400; color: var(--ink);
  }
  .footer {
    position: absolute; left: 0; top: 770px; width: 100%; height: 91px;
    background: var(--teal);
  }
  .cta {
    position: absolute; left: 124px; top: 742px; width: 360px; height: 60px;
    border-radius: 30px; background: var(--green);
    border: 4px solid var(--paper);
    display: flex; align-items: center; justify-content: center;
    font-size: 22.5px; font-weight: 700; color: var(--paper);
  }
  .contact {
    position: absolute; top: 818px; width: 100%; text-align: center;
    font-size: 16.5px; font-weight: 400; color: var(--paper);
  }
</style>
</head>
<body>
  <main class="poster">
    <header class="header">
      <div class="brand">
        <span class="brand-dot"></span>
        <span class="brand-name">Solvita</span>
      </div>
      <div class="brand-tagline">MEDIZINISCHE PODOLOGIE</div>
    </header>

    <h1 class="headline">Ihre Füsse. Unsere Kompetenz</h1>
    <p class="intro">Medizinische Fussbehandlungen für Ihre<br>Gesundheit und Lebensqualität.</p>

    <ul class="services">
      <li class="service"><span class="service-icon" role="img" aria-label="Liniensymbol zweier Fusssohlen"></span><span class="service-name">Medizinische Fusspflege</span></li>
      <li class="service"><span class="service-icon" role="img" aria-label="Liniensymbol eines Zehennagels mit seitlichen Pfeilen"></span><span class="service-name">Nagelkorrektur</span></li>
      <li class="service"><span class="service-icon" role="img" aria-label="Liniensymbol eines eingewachsenen Zehennagels"></span><span class="service-name">Eingewachsene Nägel</span></li>
      <li class="service"><span class="service-icon" role="img" aria-label="Liniensymbol von Hornhaut und Hühneraugen"></span><span class="service-name">Hornhaut &amp; Hühneraugen</span></li>
      <li class="service"><span class="service-icon" role="img" aria-label="Liniensymbol eines Fusses mit Blutstropfen"></span><span class="service-name">Diabetische Fussversorgung</span></li>
    </ul>

    <p class="audience">Auch für Risikopatienten, Kinder und Sportler</p>
    <p class="credentials">Zertifizierte Podologen | Fachgerecht - Hygienisch - Modern</p>

    <footer class="footer">
      <p class="contact">Telefonnummer XXX | solvita-podo.ch | Adresse XXX</p>
    </footer>
    <div class="cta">Jetzt Termin vereinbaren</div>
  </main>
</body>
</html>
```